依頼詳細
近隣のタワーマンションや、ホテル、貸会議室など、中高年層方々向けにチラシを置いてもらう、紹介してもらおうと考えております。シンプル、シックで上品な感じ、尚且つ、目を引く雰囲気にしていただけたらと思います。
記載項目
店名/Lorendal ロレンダール イタリアンダイニングレストラン
電話番号/06-6481-5926
住所:大阪市中央区緑岡町5-4-1 ミネハ紡第三ビル 地下1階
営業時間(Lunch:11:45-14:00、Dinner:17:30~23:30)
ランチメニュー【パスタランチ】¥800~
ディナーメニュー (アンティパスト¥1000~、ピザ.パスタ ¥1400~ お肉、お魚料理 ¥1800~、デザート¥600~)
添付写真イメージ
サイズ
A6
ページ数
両面
希望イメージ
シンプル 複雑
単色 カラフル
暗い 明るい
日常 高級
遊び心 厳粛
未来的 伝統的
女性的 男性的
希望する色
黒、白、ゴールド、木目などの茶色
納品ファイル
• 高解像度JPG (.jpg)
• イラストレーター形式 (.ai)
補足説明
写真や地図などは多少修正して頂いても、使わなくても結構です。
地図は添付の写真を参考にしていただければと思います。
とにかく、わかりやすく、ウリが的確に伝わるようにお願い致します。

```html
<!DOCTYPE html>
<html lang="ja">
<head>
<meta charset="utf-8">
<title>Lorendal イタリアンダイニングレストラン</title>
<link rel="stylesheet" href="https://fonts.googleapis.com/css2?family=Shippori+Mincho:wght@500;700&family=Zen+Kaku+Gothic+New:wght@700&display=swap">
<style>
  :root {
    --gold-light: #d8c594;
    --gold-mid: #b9a06a;
    --gold-deep: #8f7745;
    --cream: #fbf6e8;
    --white: #ffffff;
    --ink-shadow: rgba(60, 40, 10, 0.55);
    --wood-light: #c9a57c;
    --wood-dark: #6e4a2c;
  }
  * { margin: 0; padding: 0; box-sizing: border-box; }
  html, body {
    width: 851px;
    height: 1200px;
    overflow: hidden;
    background: var(--cream);
  }
  .flyer {
    position: relative;
    width: 851px;
    height: 1200px;
    background: var(--white);
    overflow: hidden;
  }
  .flyer__ground {
    position: absolute;
    inset: 26px;
    background: linear-gradient(160deg, var(--gold-light) 0%, var(--gold-mid) 45%, var(--gold-deep) 100%);
  }
  .flyer__frame {
    position: absolute;
    inset: 0;
  }
  .brand {
    position: absolute;
    top: 300px;
    left: 0;
    width: 100%;
    text-align: center;
    color: var(--white);
    text-shadow: 0 2px 4px var(--ink-shadow);
  }
  .brand__name {
    font-family: "Shippori Mincho", serif;
    font-weight: 500;
    font-size: 104px;
    line-height: 1;
    letter-spacing: 2px;
  }
  .brand__kana {
    margin-top: 8px;
    font-family: "Shippori Mincho", serif;
    font-weight: 500;
    font-size: 15px;
    letter-spacing: 4px;
  }
  .brand__genre {
    margin-top: 18px;
    font-family: "Zen Kaku Gothic New", sans-serif;
    font-weight: 700;
    font-size: 22px;
    letter-spacing: 2px;
  }
  .intro {
    position: absolute;
    top: 515px;
    left: 0;
    width: 100%;
    text-align: center;
    font-family: "Shippori Mincho", serif;
    font-weight: 700;
    font-size: 22px;
    line-height: 50px;
    letter-spacing: 7px;
    color: var(--white);
    text-shadow: 0 2px 3px var(--ink-shadow);
  }
  .intro p { margin: 0; }
  .photo {
    position: absolute;
    left: 292px;
    top: 871px;
    width: 270px;
    height: 214px;
    border: 5px solid var(--cream);
    border-radius: 16px;
    background: linear-gradient(135deg, var(--wood-light) 0%, #a98259 50%, var(--wood-dark) 100%);
    box-shadow: 0 2px 6px var(--ink-shadow);
  }
</style>
</head>
<body>
  <main class="flyer">
    <div class="flyer__ground" role="img" aria-label="金色の市松模様の背景"></div>
    <svg class="flyer__frame" width="851" height="1200" viewBox="0 0 851 1200" aria-hidden="true">
      <rect x="40" y="40" width="771" height="1120" fill="none" stroke="#ffffff" stroke-width="2"/>
      <rect x="48" y="48" width="755" height="1104" fill="none" stroke="#ffffff" stroke-opacity="0.6" stroke-width="1"/>
    </svg>

    <header class="brand">
      <h1 class="brand__name">Lorendal</h1>
      <p class="brand__kana">ロレンダール</p>
      <p class="brand__genre">イタリアンダイニングレストラン</p>
    </header>

    <section class="intro">
      <p>オフィス街の真ん中に</p>
      <p>隠れ家の雰囲気を醸し出す</p>
      <p>イタリアンダイニングレストラン</p>
      <p>ワインの神、バッカスの石膏像がお迎え</p>
      <p>至福の時をおもてなしいたします。</p>
    </section>

    <div class="photo" role="img" aria-label="店舗入口の看板の写真"></div>
  </main>
</body>
</html>
```